Website for legal services (estates law) called KTV ESTATES LAW

Simple, catchy and easy to use. I am providing estates legal services and I want clients to feel a warm, friendly but professional vibe when they visit my website. I don't want harsh legal pictures (like a picture of a tough lawyer, or pictures of scales of justice). Pictures of books, plants, signing documents or a comfortable looking office are acceptable.

Please use wordpress to design it because I want ability to upload blogs on my own through wordpress after. I am attaching my logo.

Target Market(s)

Millenials, boomers, people in their 40's and anyone looking to transfer property titles or create a will, or anyone whose relatives have died and need help with estates administration.

Industry/Entity Type

Law Firm

Coding

Coded - Design and coding required

Number of Pages Required

4 page

Font styles to use
Sans Serif

Colors
0493ce
33a6d7
85cae6
cee9f5
f4fafd

Requirements
Must have
• - Must be designed with WordPress
- Must have a warm, friendly, professional vibe
- I want to be able to edit any of the content of the website myself
Nice to have
• Pictures of law books, plants, signing documents or a comfortable looking office are acceptable.
Should not have
• I don't want harsh legal pictures (like a picture of a tough lawyer, or pictures of scales of justice).

```html
<!DOCTYPE html>
<html lang="en">
<head>
<meta charset="utf-8">
<title>KTV Estates Law</title>
<link rel="stylesheet" href="https://fonts.googleapis.com/css2?family=Lato:wght@400&family=Raleway:ital,wght@0,300;0,400;0,500;0,600;0,700;1,300;1,400;1,500&display=swap">
<style>
:root{
  --brand:#0493ce;
  --brand-mid:#33a6d7;
  --brand-light:#85cae6;
  --tint:#cee9f5;
  --pale:#f4fafd;
  --ink:#333333;
  --ink-soft:#555555;
  --white:#ffffff;
  --hero-top:#4a4b50;
  --hero-bottom:#2f3034;
  --footer:#3e3f44;
  --line:#8a8a8a;
}
*{margin:0;padding:0;box-sizing:border-box}
html,body{width:1200px;height:4063px;overflow:hidden}
body{position:relative;font-family:'Raleway',sans-serif;font-weight:300;color:var(--ink);background:var(--white)}
.abs{position:absolute}
.display{font-family:'Raleway',sans-serif;font-weight:400;font-style:italic}

/* hero */
.hero{left:0;top:0;width:1200px;height:763px;background:linear-gradient(180deg,var(--hero-top) 0%,#5c5e63 45%,#3a3b3f 75%,var(--hero-bottom) 100%)}
.brand{left:95px;top:140px;display:flex;align-items:center;gap:10px;color:var(--white);font-size:18px;font-weight:500;letter-spacing:1px}
.brand-mark{width:16px;height:16px;background:var(--white)}
.nav{left:0;top:53px;color:var(--white);font-size:17px;font-weight:400}
.nav a{color:inherit;text-decoration:none;position:absolute;white-space:nowrap}
.hero-kicker{top:276px;width:1200px;text-align:center;color:var(--white);font-size:42px;letter-spacing:2px}
.hero-title{top:328px;width:1200px;text-align:center;color:var(--white);font-size:78px;font-weight:400;font-style:italic}
.hero-sub{top:450px;width:1200px;text-align:center;color:var(--white);font-size:41px;letter-spacing:1px}
.hero-btn{left:467px;top:630px;width:265px;padding-bottom:12px;border-bottom:1px solid #cfcfcf;text-align:center;color:var(--white);font-size:15px;font-weight:600;letter-spacing:.3px}

/* welcome */
.welcome{left:0;top:763px;width:1200px;height:371px;background:var(--brand);color:var(--white);text-align:center}
.welcome p{position:absolute;width:1200px;left:0;font-size:19px;line-height:36px;top:77px}
.welcome .quote{top:205px;font-size:33px;line-height:42px;font-weight:400;font-style:italic}

/* about + services */
.paper{left:0;top:1134px;width:1200px;height:1509px;background:linear-gradient(180deg,#ffffff 0%,var(--pale) 100%)}
.plant{left:900px;top:1600px;width:300px;height:1043px;background:radial-gradient(ellipse at 100% 60%,rgba(90,130,80,.45) 0%,rgba(120,160,100,.2) 45%,rgba(255,255,255,0) 75%)}
.plant-low{left:0;top:2440px;width:1200px;height:203px;background:radial-gradient(ellipse at 45% 100%,rgba(90,130,80,.35) 0%,rgba(120,160,100,.12) 50%,rgba(255,255,255,0) 80%)}
.section-title{color:var(--brand);font-size:60px}
.about-title{left:96px;top:1228px}
.about-copy{left:96px;top:1340px;width:590px;font-size:15.5px;line-height:23px;font-weight:400;color:var(--ink)}
.about-link{left:96px;top:1566px;width:265px;padding-bottom:10px;border-bottom:1px solid var(--line);font-size:15px;font-weight:600;color:var(--brand)}
.portrait{left:743px;top:1246px;width:361px;height:344px;background:linear-gradient(160deg,#c9cdd1 0%,#9aa2aa 55%,#3c4250 100%)}

.services{left:96px;top:1705px;width:1009px;height:831px;background:var(--white)}
.services-title{top:50px;width:100%;text-align:center}
.services-intro{top:168px;width:100%;text-align:center;font-size:15px;line-height:24px;font-weight:400}
.tabs{top:376px;left:74px;font-size:18px;font-weight:600}
.tab-active{color:var(--brand)}
.tab{position:absolute;left:174px;top:0;white-space:nowrap;color:#9a9a9a}
.col-left{left:79px;top:442px;width:240px;font-size:15px;line-height:23px;font-weight:400}
.col-divider{left:349px;top:443px;width:1px;height:254px;background:var(--ink-soft)}
.col-right{left:393px;top:445px;width:520px;font-size:15px;line-height:23px;font-weight:400}
.col-left ul,.col-right ul{list-style:none;margin-top:16px}
.col-left li::before,.col-right li::before{content:"·";display:inline-block;width:30px}

/* blog */
.blog{left:0;top:2643px;width:1200px;height:790px;background:var(--brand)}
.blog-title{top:100px;width:100%;text-align:center;color:var(--white);font-size:60px}
.card{top:282px;width:242px;height:393px;background:var(--white)}
.card-img{width:242px;height:189px}
.card h3{font-family:'Raleway',sans-serif;font-style:italic;font-weight:500;color:var(--brand);font-size:25px;line-height:32px;padding:18px 20px 0 26px}
.card p{padding:6px 20px 0 26px;font-size:15px;line-height:23px;font-weight:400;color:var(--ink-soft)}

/* contact */
.contact-title{top:3515px;width:1200px;text-align:center}
.field{left:98px;width:509px;height:41px;border:1px solid #8c8c8c;font-family:'Lato',sans-serif;font-size:18px;color:#9a9a9a;padding:8px 14px}
.field-msg{height:112px}
.send{left:98px;top:3944px;width:167px;height:46px;border:1px solid #8c8c8c;font-family:'Lato',sans-serif;font-size:19px;text-align:center;line-height:44px;color:#222}
.info{left:639px;top:3648px;width:473px;height:282px;background:var(--brand);color:var(--white);font-size:15px;line-height:23px;font-weight:400}
.info-row{position:absolute;left:80px;display:flex;gap:28px;align-items:flex-start}
.info-row svg{flex:none}

.footer{left:0;top:4013px;width:1200px;height:50px;background:var(--footer);color:#b5b5b5;font-size:11px;text-align:center;line-height:62px}
</style>
</head>
<body>

<section class="abs hero" role="img" aria-label="Black and white city skyline across the water with a tall tower"></section>
<div class="abs brand"><span class="brand-mark"></span>KTV ESTATES LAW</div>
<nav class="abs nav">
  <a style="left:553px">HOME</a>
  <a style="left:653px">ABOUT</a>
  <a style="left:758px">SERVICES</a>
  <a style="left:888px">BLOG</a>
  <a style="left:981px">CONTACT</a>
</nav>
<div class="abs hero-kicker">HIGH QUALITY</div>
<h1 class="abs hero-title">legal experience</h1>
<div class="abs hero-sub">FOR ESTATES AND REAL ESTATE CLIENTS</div>
<div class="abs hero-btn">BOOK A FREE CONSULTATION</div>

<section class="abs welcome">
  <p>Thank you for visiting KTV Estates Law,<br>where I endeavor to earn your trust and provide you with high quality estates and real<br>estate law services.</p>
  <p class="quote">My goal is to make you feel comfortable<br>as soon as you step foot in my office.</p>
</section>

<section class="abs paper"></section>
<div class="abs plant" role="img" aria-label="Green plant leaves on a light background"></div>
<div class="abs plant-low" role="img" aria-label="Long green leaves along the bottom edge"></div>

<h2 class="abs section-title display about-title">about</h2>
<div class="abs about-copy">
  <p>My name is Daria Velman and I am an estates and real estate lawyer. I graduated from Northfield University Faculty of Law and my passion is estates law and real estate law.<br>Prior to entering the legal profession, I obtained my CPA (Chartered Professional Accounting) designation and worked in business and management accounting for many years, where I developed a deeper understanding of money and finances.</p>
  <p style="margin-top:23px">As a lawyer, I lean on this foundation frequently for the benefit of my clients.</p>
</div>
<div class="abs about-link">FOLLOW ME ON PROLINK</div>
<div class="abs portrait" role="img" aria-label="Portrait photo of the lawyer in a dark blazer"></div>

<section class="abs services">
  <h2 class="abs section-title display services-title">Services</h2>
  <div class="abs services-intro">I use my accounting background to provide a high quality legal experience for my<br>estates and real estate clients.<br><span style="display:inline-block;margin-top:12px">Here are the services I provide:</span></div>
  <div class="abs tabs"><span class="tab-active">Estates Law</span><span class="tab">Real Estates Law</span></div>
  <div class="abs col-left">
    <p style="font-size:16px">I offer the following services as part of an estate plan:</p>
    <ul>
      <li>Wills (personal, corporate, foreign property);</li>
      <li>Trusts;</li>
      <li>Powers of Attorney for Personal Care and Property;</li>
      <li>Asset planning to minimize income tax and estate administration tax upon your passing.</li>
    </ul>
  </div>
  <div class="abs col-divider"></div>
  <div class="abs col-right">
    <p style="font-size:16px">I help administer entire estates including:</p>
    <ul>
      <li>Guide the executor with the administration of an entire estate;</li>
      <li>Apply for the Certificate of Appointment of Estate Trustee with/without a Will (Applying for Probate);</li>
      <li>Administer trusts;</li>
      <li>Provide guidance about the requirements of financial institutions, the government, the courts;</li>
      <li>Draft documents required in dealing with various institutions;</li>
      <li>Applying for the National Pension Plan Death Benefit;</li>
      <li>Applying for the Estate Information Return.</li>
    </ul>
  </div>
</section>

<section class="abs blog">
  <h2 class="abs blog-title display">Blog</h2>
  <article class="abs card" style="left:98px">
    <div class="card-img" role="img" aria-label="Hand signing a document with a fountain pen" style="background:linear-gradient(135deg,#d8dadc,#b8bcc0 60%,#e4d3c4)"></div>
    <h3>Making a Will</h3>
    <p>Donec rutrum congue leo eget malesuada. Mauris blandit aliquet elit, eget tincidunt nibh pulvinar a. Curabitur arcu erat, ac-</p>
  </article>
  <article class="abs card" style="left:356px">
    <div class="card-img" role="img" aria-label="Open book in front of library shelves" style="background:linear-gradient(180deg,#6b5a4a,#9a7f63 55%,#d9c6aa)"></div>
    <h3>Interesting facts</h3>
    <p>Donec rutrum congue leo eget malesuada. Mauris blandit aliquet elit, eget tincidunt nibh pulvinar a. Curabitur arcu erat, ac-</p>
  </article>
  <article class="abs card" style="left:615px">
    <div class="card-img" role="img" aria-label="Stack of paper files on a desk" style="background:linear-gradient(180deg,#f1efec,#c9b59a 55%,#a98e6e)"></div>
    <h3>Interesting facts</h3>
    <p>Donec rutrum congue leo eget malesuada. Mauris blandit aliquet elit, eget tincidunt nibh pulvinar a. Curabitur arcu erat, ac-</p>
  </article>
  <article class="abs card" style="left:874px">
    <div class="card-img" role="img" aria-label="White binders on a shelf beside a small plant" style="background:linear-gradient(90deg,#f3f3f3,#dcdcdc 60%,#8f968d)"></div>
    <h3>You must read this books</h3>
    <p>Donec rutrum congue leo eget malesuada. Mauris blandit aliquet elit, eget tincidunt nibh pulvinar a.</p>
  </article>
</section>

<h2 class="abs section-title display contact-title">Contact</h2>
<div class="abs field" style="top:3648px">Name</div>
<div class="abs field" style="top:3704px">Your Email</div>
<div class="abs field" style="top:3761px">Phone Number</div>
<div class="abs field field-msg" style="top:3818px">Message</div>
<div class="abs send">SEND</div>

<aside class="abs info">
  <div class="info-row" style="top:40px">
    <svg width="40" height="40" viewBox="0 0 40 40" fill="none" stroke="#fff" stroke-width="1.6"><rect x="3" y="6" width="9" height="28" rx="3"/><rect x="12" y="9" width="24" height="25" rx="2"/><rect x="17" y="13" width="14" height="6"/><path d="M18 24h3M24 24h3M30 24h2M18 29h3M24 29h3M30 29h2"/></svg>
    <div>T: 555.280.0197<br>F: 555.694.0290</div>
  </div>
  <div class="info-row" style="top:118px">
    <svg width="40" height="40" viewBox="0 0 40 40" fill="none" stroke="#fff" stroke-width="1.6"><rect x="4" y="18" width="18" height="9" rx="4.5" transform="rotate(-40 13 22)"/><rect x="18" y="13" width="18" height="9" rx="4.5" transform="rotate(-40 27 17)"/></svg>
    <div>daria@ktv-law.ca<br>www.ktv-law.ca</div>
  </div>
  <div class="info-row" style="top:196px">
    <svg width="40" height="40" viewBox="0 0 40 40" fill="none" stroke="#fff" stroke-width="1.6"><path d="M20 22c-4-6-6-8-6-11a6 6 0 0112 0c0 3-2 5-6 11z"/><circle cx="20" cy="11" r="2"/><path d="M10 20l-6 16 10-4 12 4 10-4-5-12"/></svg>
    <div>1200 Harbour Lane,<br>Suite 1901, Lakeview ON<br>L4X2B7</div>
  </div>
</aside>

<footer class="abs footer">Copyright © KTV Estate Law</footer>

</body>
</html>
```